PELMARK
stationery items
Professional
Karim Doulani
Managing Director
Corniva Plaza L27
Al Fannar Road
P.O. Box 58214
Port Selwan
kdoulani@pelmark-gulfa.com
www.pelmark-gulfa.com
looking for full stationery items (business cards, letter heads, envelopes)
LOGO
Strategic Advisory & Property Portfolio Management Services
full package of logo

```html
<!DOCTYPE html>
<html lang="en">
<head>
<meta charset="utf-8">
<title>Pelmark Stationery</title>
<link rel="stylesheet" href="https://fonts.googleapis.com/css2?family=Playfair+Display:wght@600&family=Open+Sans:wght@400;600&display=swap">
<style>
  :root {
    --backdrop: #b4b4b4;
    --paper: #ffffff;
    --brand-red: #8c1a1a;
    --red-light: #b81f22;
    --red-dark: #6b0c0f;
    --ink: #333333;
    --ink-soft: #6a6a6a;
    --shadow: rgba(0,0,0,0.18);
  }
  * { box-sizing: border-box; margin: 0; padding: 0; }
  html, body { width: 1200px; height: 655px; overflow: hidden; }
  body {
    background: var(--backdrop);
    font-family: "Open Sans", Arial, sans-serif;
    color: var(--ink);
    position: relative;
  }
  .sheet {
    position: absolute;
    background: var(--paper);
    box-shadow: 0 1px 3px var(--shadow);
  }
  .brand { position: absolute; line-height: 1; }
  .brand-name {
    display: flex; align-items: center; gap: 4px;
    font-family: "Playfair Display", Georgia, serif;
    font-weight: 600;
    color: var(--brand-red);
    letter-spacing: 0.06em;
  }
  .brand-dot {
    display: inline-block; border-radius: 50%;
    background: var(--brand-red);
  }
  .brand-tagline {
    font-size: 3.4px; color: var(--ink-soft);
    margin-top: 2px; letter-spacing: 0.02em; white-space: nowrap;
  }
  .brand.light .brand-name { color: var(--paper); }
  .brand.light .brand-dot { background: var(--paper); }
  .brand.light .brand-tagline { color: rgba(255,255,255,0.8); }

  .contact { position: absolute; font-size: 4px; line-height: 6px; color: var(--ink); white-space: nowrap; }

  /* letterhead */
  .letterhead { left: 190px; top: 12px; width: 489px; height: 636px; }
  .letterhead .brand { left: 26px; top: 44px; }
  .letterhead .brand-name { font-size: 15px; }
  .letterhead .brand-dot { width: 5px; height: 5px; }

  /* business cards */
  .card { width: 199px; height: 117px; }
  .card-front { left: 60px; top: 233px; }
  .card-back { left: 60px; top: 367px; }
  .card .brand { left: 10px; top: 12px; }
  .card .brand-name { font-size: 11px; }
  .card .brand-dot { width: 4px; height: 4px; }
  .card-holder { position: absolute; left: 10px; top: 45px; }
  .holder-name { font-size: 5.5px; font-weight: 600; }
  .holder-title { font-size: 4.5px; color: var(--ink-soft); margin-top: 1px; }
  .card-tagline {
    position: absolute; left: 0; right: 0; bottom: 14px;
    text-align: center; font-size: 4.5px; color: var(--ink-soft);
  }

  /* envelope flap side */
  .envelope-back { left: 662px; top: 84px; width: 461px; height: 240px; }
  .flap-band {
    position: absolute; left: 0; top: 0; width: 100%; height: 108px;
    background: radial-gradient(ellipse at 50% 40%, var(--red-light), var(--red-dark) 80%);
    border-radius: 0 0 34px 34px;
  }
  .envelope-back .brand { left: 50%; top: 40px; transform: translateX(-50%); text-align: center; }
  .envelope-back .brand-name { font-size: 14px; justify-content: center; }
  .envelope-back .brand-dot { width: 5px; height: 5px; }

  /* envelope address side */
  .envelope-front { left: 662px; top: 341px; width: 461px; height: 228px; }
  .envelope-front .brand { left: 22px; top: 32px; }
  .envelope-front .brand-name { font-size: 13px; }
  .envelope-front .brand-dot { width: 4px; height: 4px; }
</style>
</head>
<body>

  <section class="sheet letterhead" aria-label="Letterhead">
    <div class="brand">
      <div class="brand-name"><span class="brand-dot"></span>PELMARK</div>
      <div class="brand-tagline">Strategic Advisory &amp; Property Portfolio Management Services</div>
    </div>
    <div class="contact" style="left:26px; top:582px;">
      Corniva Plaza L27<br>Al Fannar Road<br>P.O. Box 58214, Port Selwan
    </div>
    <div class="contact" style="left:120px; top:582px;">
      T +31 20 330 1200<br>F +31 20 330 1201<br>www.pelmark-gulfa.com
    </div>
  </section>

  <section class="sheet card card-front" aria-label="Business card front">
    <div class="brand">
      <div class="brand-name"><span class="brand-dot"></span>PELMARK</div>
      <div class="brand-tagline">Strategic Advisory &amp; Property Portfolio Management</div>
    </div>
    <div class="card-holder">
      <div class="holder-name">Karim Doulani</div>
      <div class="holder-title">Managing Director</div>
    </div>
    <div class="contact" style="left:10px; top:72px;">
      T +31 20 330 1200<br>F +31 20 330 1201<br>M +31 6 612 4478
    </div>
    <div class="contact" style="left:82px; top:72px;">
      Corniva Plaza L27, Al Fannar Road<br>P.O. Box 58214, Port Selwan<br>kdoulani@pelmark-gulfa.com<br>www.pelmark-gulfa.com
    </div>
  </section>

  <section class="sheet card card-back" aria-label="Business card back">
    <div class="brand">
      <div class="brand-name"><span class="brand-dot"></span>PELMARK</div>
      <div class="brand-tagline">Strategic Advisory &amp; Property Portfolio Management</div>
    </div>
    <p class="card-tagline">Strategic Advisory &amp; Property Portfolio Management Services</p>
  </section>

  <section class="sheet envelope-back" aria-label="Envelope flap side">
    <div class="flap-band"></div>
    <div class="brand light">
      <div class="brand-name"><span class="brand-dot"></span>PELMARK</div>
      <div class="brand-tagline">Strategic Advisory &amp; Property Portfolio Management Services</div>
    </div>
  </section>

  <section class="sheet envelope-front" aria-label="Envelope address side">
    <div class="brand">
      <div class="brand-name"><span class="brand-dot"></span>PELMARK</div>
      <div class="brand-tagline">Strategic Advisory &amp; Property Portfolio Management Services</div>
    </div>
    <div class="contact" style="left:22px; top:170px;">
      Corniva Plaza L27<br>Al Fannar Road<br>P.O. Box 58214, Port Selwan
    </div>
    <div class="contact" style="left:142px; top:170px;">
      T +31 20 330 1200<br>F +31 20 330 1201<br>www.pelmark-gulfa.com
    </div>
  </section>

</body>
</html>
```